Looking for copywriting of the entire website + new selection of pictures

Hello,
My website's copy write is on the weaker side, so I'm looking for an entire re-do of my website's copy write. If you think a line is weak, re-write, otherwise you can leave it as is. We want our site to clearly explain what our events are, how they work, and why someone should sign up for them, while appealing to the hopeful, romantic, and nostalgic feelings of the visitors. Our speed dating events can be imagined as a modern day approach to the old-fashioned way of dating, where people got to know each other in person, away from the dating apps!! Additionally, I feel nearly all the existing pictures are rather weak, so please select entirely new pictures which give the website a less amateur feel, while retaining the playful nature of the brand. If there are areas where you think that section would benefit from no pictures at all, please communicate that.
Let me know if there are any further questions and thank you!
You can find the site at:
https://www.lanternmeetups.com
Industry/Entity Type
Speed Dating/Romance
Number of Pages Required
1 page
Look and feel
Each slider illustrates characteristics of the customer's brand and the style your logo design should communicate.

```html
<!DOCTYPE html>
<html lang="en">
<head>
<meta charset="utf-8">
<title>Lantern Meetups</title>
<link rel="stylesheet" href="https://fonts.googleapis.com/css2?family=Nunito:ital,wght@0,400;0,500;0,600;0,700;0,800;1,400&display=swap">
<style>
:root{
  --pink:#f472b6;
  --pink-faint:#fde4f0;
  --ink:#111111;
  --text:#2b2b2b;
  --field:#f3f3f3;
  --white:#ffffff;
}
*{box-sizing:border-box;margin:0;padding:0}
html,body{width:1200px;height:4158px;overflow:hidden;background:var(--white)}
body{position:relative;font-family:"Nunito",sans-serif;color:var(--text)}
.abs{position:absolute}
.pink{color:var(--pink)}
.btn{position:absolute;display:flex;align-items:center;justify-content:center;background:var(--pink);color:var(--white);border-radius:8px;font-size:15px;font-weight:500;text-decoration:none}

/* nav */
.site-nav{position:absolute;left:0;top:0;width:1200px;height:113px;border-bottom:2px solid var(--pink);background:var(--white)}
.nav-links{position:absolute;left:50px;top:42px;display:flex;gap:30px;font-size:16px;font-weight:500;color:var(--ink)}
.nav-brand{position:absolute;left:0;width:1200px;top:40px;text-align:center;font-size:22px;font-weight:800;color:var(--ink)}
.nav-social{position:absolute;left:828px;top:44px;display:flex;gap:40px}
.nav-social span{width:20px;height:20px;border-radius:50%;background:var(--ink);display:block}
.nav-contact{left:1005px;top:31px;width:147px;height:46px;font-size:15px}

/* hero */
.hero{position:absolute;left:0;top:115px;width:1200px;height:525px;background:linear-gradient(100deg,#2e3244 0%,#4a3a3f 40%,#8a5a4c 70%,#b98a72 100%)}
.hero-title{position:absolute;left:92px;top:230px;font-size:64px;font-weight:800;color:var(--white);letter-spacing:-1px}
.hero-sub{position:absolute;left:92px;top:318px;width:460px;font-size:26px;line-height:38px;color:var(--white)}
.hero-book{left:92px;top:431px;width:151px;height:46px}
.hero-events{position:absolute;left:269px;top:431px;width:151px;height:46px;border:2px solid var(--white);border-radius:8px;color:var(--white);display:flex;align-items:center;justify-content:center;font-size:15px}

/* shared */
.h2{font-size:46px;font-weight:600;line-height:58px;color:var(--ink)}
.body-copy{font-size:19px;line-height:30px;color:var(--text)}
.photo{position:absolute;border-radius:22px}

/* how it works */
.feature-card{position:absolute;top:1578px;width:320px;height:180px;background:var(--white);border:1px solid #f0f0f0;border-radius:6px;box-shadow:0 4px 16px rgba(0,0,0,.05);text-align:center;padding:46px 40px 0}
.feature-card h3{font-size:20px;font-weight:500;color:var(--ink);margin-bottom:14px}
.feature-card p{font-size:11.5px;line-height:18px;color:#444}
.feature-icon{position:absolute;top:-36px;left:50%;margin-left:-36px;width:72px;height:72px;border-radius:50%;background:var(--pink-faint);display:flex;align-items:center;justify-content:center}

/* steps */
.steps{position:absolute;left:92px;top:1998px;width:560px}
.steps li{list-style:none;position:relative;padding-left:33px;font-size:19px;line-height:31.5px;color:var(--text)}
.steps li svg{position:absolute;left:0;top:8px}

/* locations */
.city-select{position:absolute;left:840px;top:2397px;width:250px;height:45px;background:var(--field);font-size:15px;color:#777;padding:12px 14px}
.city-card{position:absolute;top:2562px;width:315px;height:430px;background:var(--white);border-radius:22px;box-shadow:0 6px 22px rgba(0,0,0,.06);overflow:hidden}
.city-photo{height:217px;border-radius:22px 22px 0 0}
.city-card h3{margin:14px 20px 6px;font-size:20px;font-weight:500;color:var(--pink)}
.city-card p{margin:0 20px;font-size:12px;line-height:18px;color:#333}
.city-btn{left:20px;top:370px;width:275px;height:42px;font-size:14px}

/* signup */
.signup-field{position:absolute;left:711px;width:331px;height:41px;background:var(--field);font-size:11px;color:#999;padding:14px 12px}

/* footer */
.footer-center{position:absolute;left:0;width:1200px;text-align:center}
</style>
</head>
<body>

<header class="site-nav">
  <nav class="nav-links"><span>Home</span><span>Events</span><span>How it Works</span><span>FAQ</span></nav>
  <div class="nav-brand">Lantern Meetups</div>
  <div class="nav-social" aria-label="Social links"><span></span><span></span><span></span></div>
  <a class="btn nav-contact">Contact Us</a>
</header>

<section class="hero" role="img" aria-label="Photo of a smiling woman across a restaurant table from a man">
  <h1 class="hero-title">Lantern Meetups</h1>
  <p class="hero-sub">Rediscover the Joy of Meeting People in Person</p>
  <a class="btn hero-book">Book Now</a>
  <a class="hero-events">Our Events</a>
</section>

<!-- intro -->
<svg class="abs" style="left:820px;top:640px" width="380" height="300" aria-hidden="true">
  <circle cx="330" cy="90" r="120" fill="none" stroke="#fde9f2" stroke-width="20"/>
</svg>
<h2 class="h2 abs" style="left:92px;top:748px;width:560px">Rediscover the Magic of<br><span class="pink">Lantern Meetups:</span></h2>
<p class="body-copy abs" style="left:92px;top:886px;width:520px">In a world of endless swiping, the longing for a real, face-to-face spark has never been stronger. Lantern Meetups brings back the charm of meeting someone the old-fashioned way, with a modern twist. Our speed dating events trade screens for smiles, giving you the chance to share a table, a laugh and a genuine conversation. Step away from the apps and let romance find you in the room, where every good story used to begin.</p>
<div class="photo" style="left:681px;top:760px;width:409px;height:395px;background:linear-gradient(135deg,#3a2616,#7a4a22 50%,#c48a3c)" role="img" aria-label="Photo of a couple laughing over drinks at a bar"></div>

<!-- how it works -->
<svg class="abs" style="left:0;top:1225px" width="320" height="440" aria-hidden="true">
  <circle cx="160" cy="220" r="180" fill="none" stroke="#fde4ef" stroke-width="3"/>
  <circle cx="160" cy="220" r="114" fill="none" stroke="#fde4ef" stroke-width="3"/>
</svg>
<svg class="abs" style="left:860px;top:1680px" width="340" height="260" aria-hidden="true">
  <circle cx="220" cy="150" r="130" fill="#fde8f1"/>
</svg>
<h2 class="h2 abs" style="left:0;top:1262px;width:1200px;text-align:center">How Lantern Meetups<br><span class="pink">Works</span></h2>
<p class="body-copy abs" style="left:330px;top:1399px;width:540px;text-align:center">Real connections happen naturally at Lantern Meetups. Every evening is built around honest, relaxed conversation with new people. Here's how it unfolds:</p>

<div class="feature-card" style="left:92px">
  <div class="feature-icon"><svg width="34" height="34" viewBox="0 0 34 34"><circle cx="12" cy="20" r="7" fill="none" stroke="#f472b6" stroke-width="3"/><circle cx="23" cy="12" r="7" fill="none" stroke="#f472b6" stroke-width="3"/></svg></div>
  <h3>Simplicity is Key</h3>
  <p>No hosts, no name tags, no pressure. Just a warm, easygoing room where everyone can relax and be themselves.</p>
</div>
<div class="feature-card" style="left:432px">
  <div class="feature-icon"><svg width="34" height="34" viewBox="0 0 34 34"><path d="M4 6h22v15H14l-7 6v-6H4z" fill="#f472b6"/></svg></div>
  <h3>Organic Conversations</h3>
  <p>Each event has 7 rounds of 10 minutes, enough time to move past small talk, share a story and see if there's a real spark between you.</p>
</div>
<div class="feature-card" style="left:771px">
  <div class="feature-icon"><svg width="34" height="34" viewBox="0 0 34 34"><rect x="8" y="5" width="18" height="25" rx="4" fill="#f472b6"/></svg></div>
  <h3>Casual Code</h3>
  <p>Come as you are. Casual dress and laid-back chats keep the mood light, friendly and comfortable for everyone at the table.</p>
</div>

<!-- seamless -->
<h2 class="h2 abs" style="left:92px;top:1876px;width:600px"><span class="pink">Seamless</span> Event Structure</h2>
<p class="body-copy abs" style="left:92px;top:1955px">Your evening is as simple as:</p>
<ul class="steps">
  <li><svg width="17" height="15" viewBox="0 0 17 15"><path d="M8.5 15 1.5 8A4 4 0 0 1 8.5 2a4 4 0 0 1 7 6z" fill="#f472b6"/></svg>Arrive at your chosen venue at your set time.</li>
  <li><svg width="17" height="15" viewBox="0 0 17 15"><path d="M8.5 15 1.5 8A4 4 0 0 1 8.5 2a4 4 0 0 1 7 6z" fill="#f472b6"/></svg>Receive a personal schedule with the start and end time of every round,</li>
  <li><svg width="17" height="15" viewBox="0 0 17 15"><path d="M8.5 15 1.5 8A4 4 0 0 1 8.5 2a4 4 0 0 1 7 6z" fill="#f472b6"/></svg>plus a short description of who you'll meet.</li>
  <li><svg width="17" height="15" viewBox="0 0 17 15"><path d="M8.5 15 1.5 8A4 4 0 0 1 8.5 2a4 4 0 0 1 7 6z" fill="#f472b6"/></svg>Find your date, take a seat, and say hello.</li>
  <li><svg width="17" height="15" viewBox="0 0 17 15"><path d="M8.5 15 1.5 8A4 4 0 0 1 8.5 2a4 4 0 0 1 7 6z" fill="#f472b6"/></svg>After each round, text back a Match (M) or a Pass (P), privately.</li>
  <li><svg width="17" height="15" viewBox="0 0 17 15"><path d="M8.5 15 1.5 8A4 4 0 0 1 8.5 2a4 4 0 0 1 7 6z" fill="#f472b6"/></svg>Relax, enjoy the night and let sparks fly!</li>
</ul>
<div class="photo" style="left:681px;top:1882px;width:409px;height:396px;background:linear-gradient(150deg,#1c2430,#3b3a44 45%,#8c6a4a)" role="img" aria-label="Photo of friends toasting with champagne glasses"></div>

<!-- locations -->
<svg class="abs" style="left:960px;top:2450px" width="240" height="300" aria-hidden="true">
  <circle cx="230" cy="150" r="140" fill="none" stroke="#fde4ef" stroke-width="3"/>
</svg>
<h2 class="h2 abs" style="left:92px;top:2390px">Event <span class="pink">Locations:</span></h2>
<div class="city-select">Select your city
  <svg class="abs" style="right:16px;top:18px" width="12" height="8" viewBox="0 0 12 8"><path d="M1 1l5 5 5-5" fill="none" stroke="#777" stroke-width="1.6"/></svg>
</div>
<p class="abs" style="left:92px;top:2474px;font-size:19px;color:var(--ink)">Showing every city hosting events in the United States</p>

<article class="city-card" style="left:92px">
  <div class="city-photo" role="img" aria-label="Photo of the New York skyline at sunset" style="background:linear-gradient(180deg,#e8a06a,#b0787a 55%,#3f4a5a)"></div>
  <h3>New York</h3>
  <p>Eight million stories, and yours could start here. Swap the subway stare for a real smile and meet singles who love this city as much as you do.</p>
  <a class="btn city-btn">Show Events</a>
</article>
<article class="city-card" style="left:434px">
  <div class="city-photo" role="img" aria-label="Photo of the Jersey City waterfront at night" style="background:linear-gradient(180deg,#0e1a33,#22304a 60%,#5a5a6a)"></div>
  <h3>Jersey City</h3>
  <p>Right across the river, Jersey City is a hidden gem for singles. Share a table, a view and a conversation that could lead somewhere special.</p>
  <a class="btn city-btn">Show Events</a>
</article>
<article class="city-card" style="left:775px">
  <div class="city-photo" role="img" aria-label="Photo of the Boston skyline at dusk" style="background:linear-gradient(180deg,#2a4a8a,#4a3a7a 55%,#8a3a8a)"></div>
  <h3>Boston</h3>
  <p>The city that sparked a revolution is ready to spark one in your heart. Meet Boston singles looking for something real.</p>
  <a class="btn city-btn">Show Events</a>
</article>
<a class="btn" style="left:503px;top:3028px;width:194px;height:51px">Browse All Events</a>

<!-- signup -->
<div class="photo" style="left:92px;top:3190px;width:558px;height:449px;border-radius:8px;background:linear-gradient(135deg,#2a1c14,#6a3a22 50%,#a66a3a)" role="img" aria-label="Photo of a smiling couple in winter hats holding glasses of red wine"></div>
<h2 class="abs" style="left:711px;top:3190px;width:300px;font-size:40px;line-height:54px;font-weight:500;color:#333">Now is the time to get together!</h2>
<p class="abs" style="left:711px;top:3315px;width:320px;font-size:12px;line-height:20px;color:#333">Put the phone down and meet someone the old-fashioned way. The best moments happen face to face, and your next great story is just one evening away.</p>
<div class="signup-field" style="top:3416px">Email</div>
<div class="signup-field" style="top:3476px">Password</div>
<a class="btn" style="left:711px;top:3537px;width:331px;height:42px;font-size:14px">Join Lantern Meetups</a>
<p class="abs" style="left:711px;top:3603px;width:260px;font-size:11px;line-height:19px;color:#999">*By signing up you agree to our terms &amp; conditions and privacy &amp; cookies policy</p>

<!-- footer -->
<footer>
  <div class="footer-center" style="top:3785px;font-size:26px;font-weight:800;color:var(--ink)">Lantern Meetups</div>
  <h2 class="footer-center" style="top:3880px;font-size:40px;font-weight:500;color:var(--ink)">Contact</h2>
  <div class="footer-center" style="top:3956px;font-size:21px;color:#555">
    <svg width="12" height="10" viewBox="0 0 12 10" style="margin-right:10px"><rect x="0.5" y="0.5" width="11" height="9" fill="none" stroke="#aaa"/><path d="M1 1l5 4 5-4" fill="none" stroke="#aaa"/></svg>welcome@lanternmeetups.com
  </div>
  <div class="footer-center" style="top:3999px;font-size:21px;color:#555">
    <svg width="12" height="12" viewBox="0 0 12 12" style="margin-right:10px"><path d="M2 1l2 0 1 3-1.5 1a7 7 0 0 0 3.5 3.5L8 7l3 1v2a1 1 0 0 1-1 1A9 9 0 0 1 1 2a1 1 0 0 1 1-1z" fill="none" stroke="#aaa"/></svg>(201) 555-0147
  </div>
  <div class="footer-center" style="top:4049px;font-size:21px;font-style:italic;color:#555">Copyright © 2023 Lantern Meetups. All Rights Reserved.</div>
</footer>

</body>
</html>
```